Luxury Brand Coffee Table Book Template

Overview:
We are creating a premium, 28-page coffee table book to accompany every bespoke jewelry piece handcrafted by Vellmoor Jewelry. This book serves as an heirloom that documents the story, design, and craftsmanship behind each custom piece, culminating in a powerful legacy statement. We need a refined, luxurious, and masculine layout template that can be updated for each new customer.
**All reference files (images, logos, copy for pages, etc.) are included in the .zip file.
Deliverables:
Print-ready 28-page InDesign or editable template file
Front and back cover design
Consistent typography and page layouts based on our outlined structure
Design system that allows for easy photo and text updates per client
Specs:
Size: 8.1 x 10.6 in, Portrait Orientation
Cover: Black linen hardcover with gold foil stamped name or crest (simulated in mockup)
Interior: Deep matte photo paper feel – minimalistic, clean layout with generous whitespace
Color Palette: Black, white, and gold
Style: Bold, masculine, timeless, high-luxury (think Karvane Studio x Dellbrook & Co.)
See the attached 28-page outline. Please use stock image placeholders for now.
Target Market(s)
Affluent Men & Women age 35-65
Industry/Entity Type
Luxury Retail Jewelry
Font styles to use
Other font styles liked:
- I really like Trajan Pro 3, but open to suggestions, as well as a mixture of Serif and Sans Serif fonts
Look and feel
Each slider illustrates characteristics of the customer's brand and the style your logo design should communicate.

```html
<!DOCTYPE html>
<html lang="en">
<head>
<meta charset="utf-8">
<title>Vellmoor Jewelry — Book Spreads</title>
<link rel="stylesheet" href="https://fonts.googleapis.com/css2?family=Playfair+Display:wght@700;800;900&family=Poppins:wght@400;500&display=swap">
<style>
  :root{
    --bg:#e4e4e4;
    --paper:#f3f3f3;
    --ink:#141414;
    --gold:#b8690f;
    --gold-deep:#a65c0a;
    --muted:#3a3a3a;
    --rule:#222;
  }
  *{box-sizing:border-box;margin:0;padding:0}
  html,body{width:857px;height:1200px;overflow:hidden;background:var(--bg)}
  body{position:relative;font-family:"Poppins",sans-serif;color:var(--ink)}
  .spread{position:absolute;left:20px;width:817px;height:534px;display:flex;box-shadow:0 6px 18px rgba(0,0,0,.18)}
  .spread--catalog{top:36px}
  .spread--craft{top:624px}
  .page{position:relative;width:408.5px;height:534px;background:var(--paper);overflow:hidden}
  .page--left{background:linear-gradient(90deg,var(--paper) 88%,#e2e2e2)}
  .page--right{background:linear-gradient(90deg,#e0e0e0,var(--paper) 10%)}
  .folio{position:absolute;bottom:18px;right:34px;font-family:"Playfair Display",serif;font-size:7px}
  .photo{position:absolute;display:block}

  /* product grid */
  .card{position:absolute;width:110px}
  .card .photo{position:relative;width:110px;height:64px}
  .card__title{font-family:"Playfair Display",serif;font-weight:800;font-size:7.5px;margin:7px 0 4px 4px}
  .card__text{font-size:4.2px;line-height:1.45;color:var(--muted);padding:0 6px 0 8px;height:20px}
  .card__price{margin-top:6px;background:var(--gold);color:#fff;font-family:"Playfair Display",serif;font-size:6px;padding:1.5px 6px;height:9px;line-height:6px}
  .card__amount{text-align:right;font-size:4.5px;margin-top:3px;padding-right:4px}
  .tone-ring{background:linear-gradient(160deg,#c9b18c 0%,#4a3b30 35%,#1e1a1a 70%,#3a3638)}
  .tone-gold{background:linear-gradient(160deg,#f3b24a,#c9780f 55%,#8a4a0b)}
  .tone-emerald{background:linear-gradient(150deg,#5c7590,#23384d 55%,#1a2838)}

  /* feature rows */
  .feature .photo{height:140px;width:180px;background:radial-gradient(ellipse at 60% 55%,#d9a97a,#a9703f 55%,#5b3a26)}
  .feature__text{position:absolute;width:160px}
  .feature__title{font-family:"Playfair Display",serif;font-weight:800;color:var(--gold);font-size:11.5px;line-height:1.15}
  .feature__desc{font-size:4.8px;line-height:1.5;margin-top:5px;color:var(--muted);padding-right:10px}
  .feature__price,.feature__code{font-family:"Playfair Display",serif;font-weight:700;font-size:8px;line-height:1.1}
  .feature__price{margin-top:5px}
  .feature__price span,.feature__code span{display:block;font-family:"Poppins",sans-serif;font-weight:400;font-size:8px}
  .feature__code{position:absolute;right:6px;top:84px}

  /* craft spread */
  .hero{inset:0;width:100%;height:100%;background:radial-gradient(ellipse at 45% 55%,#c49a78 0%,#7d5a3f 40%,#3b2a1e 80%,#1a130e)}
  .portrait{background:linear-gradient(170deg,#6d6556,#8d8473 45%,#d9c9b8 80%,#efe3d4)}
  .section-label{position:absolute;left:40px;top:282px;font-family:"Playfair Display",serif;font-weight:800;color:var(--gold);font-size:19px;letter-spacing:.5px}
  .section-rule{position:absolute;left:28px;top:312px;width:168px;border-top:1px solid var(--rule)}
  .statement{position:absolute;left:28px;top:336px;width:170px;font-family:"Playfair Display",serif;font-weight:900;font-size:23px;line-height:1.12}
  .body-copy{position:absolute;left:214px;top:322px;width:170px;font-size:6.2px;line-height:1.55;text-align:justify;color:var(--muted)}
  .body-copy p+p{margin-top:6px}
</style>
</head>
<body>

<section class="spread spread--catalog">
  <div class="page page--left">
    <article class="card" style="left:26px;top:30px">
      <div class="photo tone-ring" role="img" aria-label="Diamond ring on dark surface with warm bokeh"></div>
      <h3 class="card__title">Lorem Ipsum</h3>
      <p class="card__text">It is a long established fact that a reader will be distracted by the readable content of a page when looking at its layout.</p>
      <div class="card__price">Price</div><div class="card__amount">$XXX</div>
    </article>
    <article class="card" style="left:26px;top:178px">
      <div class="photo tone-ring" role="img" aria-label="Diamond ring on dark surface with warm bokeh"></div>
      <h3 class="card__title">Lorem Ipsum</h3>
      <p class="card__text">It is a long established fact that a reader will be distracted by the readable content of a page when looking at its layout.</p>
      <div class="card__price">Price</div><div class="card__amount">$XXX</div>
    </article>
    <article class="card" style="left:26px;top:326px">
      <div class="photo tone-ring" role="img" aria-label="Diamond ring on dark surface with warm bokeh"></div>
      <h3 class="card__title">Lorem Ipsum</h3>
      <p class="card__text">It is a long established fact that a reader will be distracted by the readable content of a page when looking at its layout.</p>
      <div class="card__price">Price</div><div class="card__amount">$XXX</div>
    </article>
    <article class="card" style="left:148px;top:52px">
      <div class="photo tone-gold" role="img" aria-label="Stack of ornate gold bangles"></div>
      <h3 class="card__title">Lorem Ipsum</h3>
      <p class="card__text">It is a long established fact that a reader will be distracted by the readable content of a page when looking at its layout.</p>
      <div class="card__price">Price</div><div class="card__amount">$XXX</div>
    </article>
    <article class="card" style="left:148px;top:200px">
      <div class="photo tone-gold" role="img" aria-label="Stack of ornate gold bangles"></div>
      <h3 class="card__title">Lorem Ipsum</h3>
      <p class="card__text">It is a long established fact that a reader will be distracted by the readable content of a page when looking at its layout.</p>
      <div class="card__price">Price</div><div class="card__amount">$XXX</div>
    </article>
    <article class="card" style="left:148px;top:348px">
      <div class="photo tone-gold" role="img" aria-label="Stack of ornate gold bangles"></div>
      <h3 class="card__title">Lorem Ipsum</h3>
      <p class="card__text">It is a long established fact that a reader will be distracted by the readable content of a page when looking at its layout.</p>
      <div class="card__price">Price</div><div class="card__amount">$XXX</div>
    </article>
    <article class="card" style="left:270px;top:74px">
      <div class="photo tone-emerald" role="img" aria-label="Emerald and diamond pendant on dark blue fabric"></div>
      <h3 class="card__title">Lorem Ipsum</h3>
      <p class="card__text">It is a long established fact that a reader will be distracted by the readable content of a page when looking at its layout.</p>
      <div class="card__price">Price</div><div class="card__amount">$XXX</div>
    </article>
    <article class="card" style="left:270px;top:222px">
      <div class="photo tone-emerald" role="img" aria-label="Emerald and diamond pendant on dark blue fabric"></div>
      <h3 class="card__title">Lorem Ipsum</h3>
      <p class="card__text">It is a long established fact that a reader will be distracted by the readable content of a page when looking at its layout.</p>
      <div class="card__price">Price</div><div class="card__amount">$XXX</div>
    </article>
    <article class="card" style="left:270px;top:370px">
      <div class="photo tone-emerald" role="img" aria-label="Emerald and diamond pendant on dark blue fabric"></div>
      <h3 class="card__title">Lorem Ipsum</h3>
      <p class="card__text">It is a long established fact that a reader will be distracted by the readable content of a page when looking at its layout.</p>
      <div class="card__price">Price</div><div class="card__amount">$XXX</div>
    </article>
    <span class="folio">7</span>
  </div>

  <div class="page page--right">
    <article class="feature">
      <div class="photo" style="left:40px;top:34px" role="img" aria-label="Diamond leaf necklace worn at the neckline"></div>
      <div class="feature__text" style="left:234px;top:78px">
        <h3 class="feature__title">Lorem Ipsum is<br>simply dummy text</h3>
        <p class="feature__desc">Lorem Ipsum is simply dummy text of the printing and typesetting industry.</p>
        <p class="feature__price">Price<span>$XXX</span></p>
        <p class="feature__code">Code<span>XXX</span></p>
      </div>
    </article>
    <article class="feature">
      <div class="photo" style="left:20px;top:190px" role="img" aria-label="Diamond leaf necklace worn at the neckline"></div>
      <div class="feature__text" style="left:214px;top:234px">
        <h3 class="feature__title">Lorem Ipsum is<br>simply dummy text</h3>
        <p class="feature__desc">Lorem Ipsum is simply dummy text of the printing and typesetting industry.</p>
        <p class="feature__price">Price<span>$XXX</span></p>
        <p class="feature__code">Code<span>XXX</span></p>
      </div>
    </article>
    <article class="feature">
      <div class="photo" style="left:0;top:346px" role="img" aria-label="Diamond leaf necklace worn at the neckline"></div>
      <div class="feature__text" style="left:194px;top:386px">
        <h3 class="feature__title">Lorem Ipsum is<br>simply dummy text</h3>
        <p class="feature__desc">Lorem Ipsum is simply dummy text of the printing and typesetting industry.</p>
        <p class="feature__price">Price<span>$XXX</span></p>
        <p class="feature__code">Code<span>XXX</span></p>
      </div>
    </article>
    <span class="folio">8</span>
  </div>
</section>

<section class="spread spread--craft">
  <div class="page page--left">
    <div class="photo hero" role="img" aria-label="Jeweller's hands setting stones into an ornate gold medallion on a workbench"></div>
    <span class="folio" style="color:#e8d9c6">9</span>
  </div>

  <div class="page page--right">
    <div class="photo portrait" style="left:0;top:26px;width:112px;height:200px" role="img" aria-label="Model wearing a diamond necklace, soft side view"></div>
    <div class="photo portrait" style="left:122px;top:26px;width:132px;height:238px" role="img" aria-label="Model in cream drape wearing sapphire necklace and earrings"></div>
    <div class="photo portrait" style="left:264px;top:64px;width:145px;height:240px" role="img" aria-label="Model wearing a diamond necklace, soft side view"></div>

    <h2 class="section-label">CRAFT</h2>
    <div class="section-rule"></div>
    <h1 class="statement">Lorem Ipsum is simply dummy text</h1>
    <div class="body-copy">
      <p>There are many variations of passages of Lorem Ipsum available, but the majority have suffered alteration in some form, by injected humour, or randomised words which don't look even slightly believable. If you are going to use a passage of Lorem Ipsum, you need to be sure there isn't anything embarrassing hidden in the middle of text.</p>
      <p>Lorem Ipsum is simply dummy text of the printing and typesetting industry. Lorem Ipsum has been the industry's standard dummy text ever since the 1500s, when an unknown printer took a galley of type and scrambled it to make a type specimen book.</p>
    </div>
    <span class="folio">10</span>
  </div>
</section>

</body>
</html>
```